QUOTE Graphics for Summer Challenge

I would like to put these quotes over one of the pictures attached; For Instagram, use new size: 4:5 (1080 x 1350 pixels). One Quote per picture, and I want the quote to be bold or easy to read as well. I provided a few reference graphics that I really like as examples below.
All of the pictures are attached; you can pick any photo and add one quote to it; but no stock photography
All the quotes are in the attached WORD document

```html
<!DOCTYPE html>
<html lang="en">
<head>
<meta charset="utf-8">
<title>Sun Glow Summer Shapeup – Quote Graphics</title>
<link href="https://fonts.googleapis.com/css2?family=Barlow:ital,wght@0,300;0,400;0,600;0,700;1,700&family=Pinyon+Script&display=swap" rel="stylesheet">
<style>
  :root {
    --paper: #ffffff;
    --hot-pink: #ff00aa;
    --magenta: #ec0fb4;
    --navy: #22063f;
    --white: #ffffff;
    --veil-pink: rgba(226, 60, 160, 0.82);
    --circle-pink: rgba(236, 70, 180, 0.82);
    --tag-blue: #3d8fd6;
    --tag-violet: #7a4fd0;
    --tag-pink: #e04aa8;
    --accent-pink: #ff7fcf;
    --photo-light: #c9ccce;
    --photo-mid: #8c9094;
  }
  * { box-sizing: border-box; margin: 0; padding: 0; }
  html, body { width: 1006px; height: 1200px; overflow: hidden; background: var(--paper); }
  body { position: relative; font-family: "Barlow", Arial, sans-serif; color: var(--white); }

  .post { position: absolute; width: 411px; height: 514px; overflow: hidden; }
  .post--pool      { left: 73px;  top: 74px; }
  .post--waist     { left: 522px; top: 74px; background: var(--hot-pink); }
  .post--quote     { left: 73px;  top: 612px; background: var(--magenta); }
  .post--jumpstart { left: 522px; top: 612px; }

  .photo { position: absolute; }
  .post--pool .photo {
    inset: 0;
    background: linear-gradient(180deg, var(--photo-light) 0%, #a6a59c 22%, #8c9096 34%, var(--photo-mid) 60%, #b8bec2 100%);
  }
  .post--waist .photo {
    left: 4px; top: 20px; width: 210px; height: 494px;
    background: linear-gradient(180deg, #7d7d7d 0%, #5a5a5a 50%, #6e6e6e 100%);
    border-radius: 90px 90px 30px 30px;
  }
  .post--quote .photo {
    inset: 0;
    background: linear-gradient(100deg, #a00c84 0%, #c4119f 40%, var(--magenta) 85%);
  }
  .post--jumpstart .photo {
    inset: 0;
    background: linear-gradient(160deg, #9a9a9a 0%, #6c6c6c 40%, #b4b4b4 75%, #d2d2d2 100%);
  }

  .tag {
    position: absolute;
    font-size: 13.5px; line-height: 20px; font-weight: 400;
    padding: 0 4px; white-space: nowrap;
    background: linear-gradient(90deg, var(--tag-blue), var(--tag-violet));
  }
  .tag strong { font-weight: 700; color: var(--accent-pink); }
  .tag--lg { font-size: 15.5px; line-height: 23px; }

  .pool-quote {
    position: absolute; left: 42px; top: 208px; width: 327px; height: 94px;
    background: var(--veil-pink);
    padding: 3px 0 0 17px;
    font-size: 24px; line-height: 29.5px; font-weight: 400;
  }
  .post--pool .tag { left: 85px; top: 423px; }

  .waist-headline {
    position: absolute; left: 192px; top: 86px;
    font-size: 49px; line-height: 42px; font-weight: 700; letter-spacing: -0.3px;
  }
  .waist-headline .dark { color: var(--navy); }
  .waist-headline .light { color: var(--white); }
  .waist-script {
    position: absolute; left: 206px; top: 314px;
    font-family: "Pinyon Script", cursive; font-size: 60px; line-height: 1; color: var(--navy);
  }
  .post--waist .tag { left: 108px; top: 421px; }

  .testimonial {
    position: absolute; left: 20px; top: 228px; width: 370px;
    text-align: center; font-size: 25px; line-height: 27px; font-weight: 400;
  }
  .testimonial b { font-weight: 700; }
  .testimonial em { font-weight: 700; font-style: italic; }
  .quote-mark {
    position: absolute; font-weight: 700; font-style: italic;
    font-size: 42px; line-height: 1; color: var(--white);
  }
  .quote-mark--open  { left: 16px;  top: 218px; }
  .quote-mark--close { left: 350px; top: 288px; }
  .post--quote .tag { left: 107px; top: 421px; }

  .jump-circle {
    position: absolute; left: 126px; top: 81px; width: 276px; height: 276px;
    border-radius: 50%; background: var(--circle-pink);
  }
  .jump-text {
    position: absolute; left: 135px; top: 177px; width: 260px;
    text-align: center; font-size: 23px; line-height: 27px; font-weight: 300;
  }
  .jump-text em { font-weight: 700; font-style: italic; }
  .jump-tags { position: absolute; left: 116px; top: 429px; text-align: center; width: 190px; line-height: 0; }
  .jump-tags .tag { position: static; display: inline-block; font-size: 12.5px; line-height: 15px; padding: 0 3px; }
  .jump-tags .tag--pink { background: var(--tag-pink); margin-top: 3px; }
</style>
</head>
<body>

<section class="post post--pool">
  <div class="photo" role="img" aria-label="Photo of a woman in a black bikini wading in an infinity pool with hills behind"></div>
  <p class="pool-quote">You don’t need motivation.<br>You need a proven plan and<br>some accountability.</p>
  <p class="tag">Comment <strong>SUN GLOW</strong> to join us July 7th</p>
</section>

<section class="post post--waist">
  <div class="photo" role="img" aria-label="Cut-out black and white photo of a smiling woman in a sheer maxi cover-up, hands on hips"></div>
  <h2 class="waist-headline">
    <span class="dark">We’re</span><br>
    <span class="dark">getting a</span><br>
    <span class="light">tiny waist</span><br>
    <span class="dark">and</span><br>
    <span class="light">dropping</span><br>
    <span class="light">pounds</span>
  </h2>
  <span class="waist-script">together.</span>
  <p class="tag tag--lg">Comment <strong>SUN GLOW</strong> to join</p>
</section>

<section class="post post--quote">
  <div class="photo" role="img" aria-label="Magenta-tinted photo of a woman in a crochet top with hand on hip"></div>
  <span class="quote-mark quote-mark--open">“</span>
  <p class="testimonial">This <b>Sun Glow</b> Summer Shapeup<br>plan is <em>helping women drop</em><br><em>pounds</em> and feel <em>sexy</em> again.</p>
  <span class="quote-mark quote-mark--close">”</span>
  <p class="tag tag--lg">Comment <strong>SUN GLOW</strong> to join</p>
</section>

<section class="post post--jumpstart">
  <div class="photo" role="img" aria-label="Black and white photo of a woman in sunglasses and bikini at the edge of a pool"></div>
  <div class="jump-circle"></div>
  <p class="jump-text">If you feel like you’ve<br>let yourself go lately,<br>this is your <em>jumpstart.</em></p>
  <div class="jump-tags">
    <span class="tag">Comment SUMMER to join the</span><br>
    <span class="tag tag--pink">Sun Glow Summer Shapeup</span>
  </div>
</section>

</body>
</html>
```